Webdesign für Management Coaching
Zielgruppe
Ich bin Coach/biete Coaching-Leistungen an.
Zielgruppe: Fokus auf Führungskräfte/Entscheider/Management mit technischem Hintergrund (Forschung & Entwicklung, Engineering, Technik, Maschinenbau, Naturwissenschaften)
Coaching-Schwerpunkte: Sinn-Coaching, Begleitung bei Umbrüchen und Veränderungen (privat & beruflich), Sparring & Reflexion
Aufgabenstellung
Gewünscht wurde ein helles Design, das die Logo-Farben aufnimmt. Ausrichtung am Logo & den verwendeten Farben, Schriften
Bilder: Ich werde noch Fotos beim Fotografen machen, die eingebunden werden sollen (Profil, etc.). Bitte Anhaltspunkte nennen, worauf ich die Fotografin hinweisen soll/welche Motive ins Konzept passen.

```html
<!DOCTYPE html>
<html lang="de">
<head>
<meta charset="utf-8">
<title>Klarweg Coaching – Management Coaching</title>
<link href="https://fonts.googleapis.com/css2?family=Alegreya:ital,wght@0,400;0,500;1,400;1,500;1,700&display=swap" rel="stylesheet">
<style>
  :root{
    --slate:#5e6a7a;
    --slate-dark:#4f5b6b;
    --mist:#8ea7b8;
    --orange:#f1a14a;
    --orange-soft:#f7c898;
    --band:#f7f8fa;
    --card:#ffffff;
    --line:#b8c7d2;
  }
  *{box-sizing:border-box;margin:0;padding:0}
  html,body{width:1200px;height:2417px;overflow:hidden;background:#fff}
  body{position:relative;font-family:"Alegreya",Georgia,serif;font-style:italic;color:var(--slate)}
  .abs{position:absolute}
  a{color:inherit;text-decoration:none}

  /* header */
  .main-nav{left:123px;top:52px;display:flex;gap:30px;font-size:16px;font-weight:500;color:var(--slate)}
  .main-nav .active{color:var(--orange)}
  .brand{left:500px;top:16px;width:200px;text-align:center}
  .brand-mark{width:66px;height:66px;border:1px solid var(--line);border-radius:50%;margin:0 auto 10px}
  .brand-name{font-style:normal;font-size:14px;letter-spacing:1px;color:var(--mist)}
  .social{top:58px;display:flex;gap:14px;left:905px}
  .social span{width:16px;height:16px;border-radius:50%;background:var(--slate)}
  .btn-outline{left:969px;top:53px;height:31px;padding:0 10px;border:1px solid var(--orange);border-radius:3px;color:var(--orange);font-size:16px;font-weight:500;display:flex;align-items:center;gap:10px}

  .btn{display:inline-flex;align-items:center;gap:10px;background:var(--orange);color:#fff;font-size:16px;font-weight:700;height:30px;padding:0 10px;border-radius:3px}

  /* hero */
  .hero-photo{left:470px;top:131px;width:730px;height:446px;
    background:radial-gradient(ellipse at 75% 20%,#fbf4e2 0%,transparent 45%),
      linear-gradient(90deg,#ffffff 0%,#efece8 22%,#d9d5d0 55%,#cfcac4 80%,#e6e1da 100%)}
  .hero-title{left:123px;top:190px;font-size:49px;line-height:56px;font-weight:400;color:var(--slate)}
  .hero-sub{left:123px;top:322px;font-size:20px;line-height:28px;color:var(--mist);font-weight:500}
  .hero-btn{left:123px;top:410px}

  /* about */
  .about-photo{left:123px;top:642px;width:382px;height:464px;border-radius:6px;background:linear-gradient(135deg,#7d8590 0%,#9aa3ad 45%,#6c7a8c 100%)}
  .kicker{font-size:20px;color:var(--mist);font-weight:500}
  .section-title{font-size:41px;color:var(--slate-dark);font-weight:500}
  .about-kicker{left:613px;top:693px}
  .about-title{left:613px;top:722px}
  .about-text{left:613px;top:795px;width:465px;font-size:18px;line-height:28.2px;color:var(--slate)}
  .about-btn{left:613px;top:1026px}

  /* offer */
  .offer-band{left:0;top:1178px;width:1200px;height:591px;background:var(--band)}
  .offer-kicker{left:0;width:1200px;top:1191px;text-align:center}
  .offer-title{left:0;width:1200px;top:1220px;text-align:center}
  .offer-card{left:123px;width:464px;height:124px;background:var(--card);border-radius:6px;padding:16px 18px}
  .offer-card.current{box-shadow:0 3px 12px rgba(80,95,115,.14)}
  .offer-card .icon{height:32px}
  .offer-card h3{font-size:22px;font-weight:500;color:var(--mist);margin-top:2px}
  .offer-card p{font-size:18px;margin-top:2px}
  .card-pointer{left:587px;top:1364px;width:0;height:0;border-top:12px solid transparent;border-bottom:12px solid transparent;border-left:18px solid #fff}
  .offer-detail{left:613px;top:1312px;width:462px;height:420px;background:var(--card);border-radius:6px}
  .offer-detail p{position:absolute;left:20px;top:16px;width:422px;text-align:center;font-size:18px;line-height:28px}
  .offer-photo{left:630px;top:1424px;width:428px;height:243px;background:linear-gradient(160deg,#c8ced6 0%,#e3e6ea 40%,#aeb7c2 100%)}
  .offer-btn{left:901px;top:1685px}

  /* clients */
  .clients-kicker{left:123px;top:1832px}
  .clients-title{left:123px;top:1862px}
  .client-card{top:1936px;width:300px;height:283px;background:var(--band);border-radius:6px;padding:14px 18px}
  .client-head{display:flex;align-items:center;gap:12px}
  .avatar{width:40px;height:40px;border-radius:50%;background:#fff;display:flex;align-items:center;justify-content:center}
  .client-name{font-size:22px;font-weight:500;color:var(--mist);line-height:22px}
  .client-role{font-size:15px;color:var(--slate)}
  .quote{margin:10px 0 4px -10px;height:36px}
  .client-card p{font-size:17px;line-height:28.2px}

  /* footer */
  .footer-band{left:0;top:2292px;width:1200px;height:125px;background:var(--band)}
  .footer-brand{left:132px;top:2300px;width:100px;text-align:center}
  .footer-brand .brand-mark{width:38px;height:38px;margin-bottom:6px}
  .footer-brand .brand-name{font-size:10px;letter-spacing:.5px}
  .footer-nav{right:122px;top:2302px;display:flex;gap:30px;font-size:16px;font-weight:500}
  .footer-social{left:1018px;top:2343px;display:flex;gap:18px}
  .footer-social span{width:16px;height:16px;border-radius:50%;background:var(--slate)}
  .footer-rule{left:123px;top:2378px;width:954px;height:1px;background:var(--line)}
  .copyright{left:123px;top:2388px;font-size:15px}
  .legal{right:122px;top:2388px;display:flex;gap:28px;font-size:15px}
</style>
</head>
<body>

<header>
  <nav class="abs main-nav">
    <a class="active" href="#">Home</a><a href="#">Leistungen</a><a href="#">Über mich</a><a href="#">Blog</a>
  </nav>
  <div class="abs brand">
    <div class="brand-mark"></div>
    <div class="brand-name">KLARWEG COACHING</div>
  </div>
  <div class="abs social"><span></span><span></span></div>
  <a class="abs btn-outline" href="#">Kontakt
    <svg width="18" height="14" viewBox="0 0 18 14" fill="none" stroke="#f1a14a" stroke-width="1.2"><path d="M2 2h9v6H6l-3 3V8H2z"/><path d="M12 5h4v6h-1v2l-2-2H9V9"/></svg>
  </a>
</header>

<section class="hero">
  <div class="abs hero-photo" role="img" aria-label="Foto: Frau sitzt auf einem Felsen im Gegenlicht über den Bergen"></div>
  <h1 class="abs hero-title">Lorem ipsum dolor<br>sit amen</h1>
  <p class="abs hero-sub">Lorem ipsum dolor sit amen,<br>consetetur sadipscing elitr</p>
  <a class="abs btn hero-btn" href="#">Termin buchen
    <svg width="12" height="12" viewBox="0 0 12 12" fill="none" stroke="#fff" stroke-width="1"><rect x="1" y="2" width="10" height="9"/><path d="M1 5h10M4 1v2M8 1v2"/><rect x="3" y="7" width="2" height="2"/></svg>
  </a>
</section>

<section class="about">
  <div class="abs about-photo" role="img" aria-label="Porträtfoto des Coachs"></div>
  <p class="abs kicker about-kicker">Ein bisschen zu mir</p>
  <h2 class="abs section-title about-title">Hi, ich bin Tobias</h2>
  <p class="abs about-text">Lorem ipsum dolor sit amet, consetetur sadipscing elitr, sed diam nonumy eirmod tempor invidunt ut labore et dolore magna aliquyam erat, sed diam voluptua. At vero eos et accusam et justo duo dolores et ea rebum. Stet clita kasd gubergren, no sea takimata sanctus est Lorem ipsum dolor sit amet. Lorem ipsum dolor sit amet, consetetur sadipscing elitr, sed diam nonumy eirmod tempor invidunt</p>
  <a class="abs btn about-btn" href="#">Mehr über mich
    <svg width="24" height="12" viewBox="0 0 24 12" fill="none" stroke="#fff" stroke-width="1.5"><path d="M1 6h21M17 1l5 5-5 5"/></svg>
  </a>
</section>

<section class="offer">
  <div class="abs offer-band"></div>
  <p class="abs kicker offer-kicker">Lorem ipsum</p>
  <h2 class="abs section-title offer-title">Mein Angebot für Dich</h2>

  <div class="abs offer-card current" style="top:1312px">
    <svg class="icon" width="32" height="32" viewBox="0 0 32 32"><circle cx="16" cy="16" r="14" fill="#f7c898"/><circle cx="16" cy="16" r="6" fill="#fff"/><path d="M16 2a14 14 0 0 1 12 7l-9 4z M30 16a14 14 0 0 1-7 12l-4-9z M16 30a14 14 0 0 1-12-7l9-4z M2 16a14 14 0 0 1 7-12l4 9z" fill="#f1a14a"/></svg>
    <h3>Sinn-Coaching</h3>
    <p>Lorem ipsum dolor sit amet, consetetur</p>
  </div>
  <div class="abs card-pointer"></div>

  <div class="abs offer-card" style="top:1460px">
    <svg class="icon" width="40" height="32" viewBox="0 0 40 32" fill="none" stroke-width="4" stroke-linecap="round"><path d="M20 6h-6a8 8 0 0 0-8 8v8" stroke="#f7c898"/><path d="M38 6H22" stroke="#f1a14a"/><path d="M2 16h36" stroke="#f1a14a"/><path d="M20 26h18" stroke="#f7c898"/></svg>
    <h3>Begleitung bei Veränderung</h3>
    <p>Lorem ipsum dolor sit amet, consetetur</p>
  </div>

  <div class="abs offer-card" style="top:1608px">
    <svg class="icon" width="36" height="32" viewBox="0 0 36 32"><path d="M18 2c9 0 16 6 16 13s-7 13-16 13c-3 0-5-.5-7-1l-8 3 3-7C3 21 2 18 2 15 2 8 9 2 18 2z" fill="#f7c898"/><circle cx="13" cy="13" r="2" fill="#f1a14a"/><circle cx="23" cy="13" r="2" fill="#f1a14a"/><path d="M11 18q7 6 14 0" stroke="#f1a14a" stroke-width="2" fill="none"/></svg>
    <h3>Sparring &amp; Reflexion</h3>
    <p>Lorem ipsum dolor sit amet, consetetur</p>
  </div>

  <div class="abs offer-detail">
    <p>Lorem ipsum dolor sit amet, consetetur sadipscing elitr, sed diam nonumy eirmod tempor invidunt ut labore et dolore magna aliquyam erat, sed diam</p>
  </div>
  <div class="abs offer-photo" role="img" aria-label="Foto: offene Hand mit schwebender Wortwolke rund um Coaching"></div>
  <a class="abs btn offer-btn" href="#">Mehr erfahren
    <svg width="24" height="12" viewBox="0 0 24 12" fill="none" stroke="#fff" stroke-width="1.5"><path d="M1 6h21M17 1l5 5-5 5"/></svg>
  </a>
</section>

<section class="clients">
  <p class="abs kicker clients-kicker">Lorem ipsum</p>
  <h2 class="abs section-title clients-title">More happy Clients...</h2>

  <article class="abs client-card" style="left:123px">
    <div class="client-head"><div class="avatar"><svg width="22" height="22" viewBox="0 0 22 22" fill="#5e6a7a"><circle cx="11" cy="7" r="5"/><path d="M1 22c0-6 4-9 10-9s10 3 10 9z"/></svg></div>
      <div><div class="client-name">Max Muster</div><div class="client-role">Sample Manager</div></div></div>
    <svg class="quote" width="48" height="36" viewBox="0 0 48 36"><path d="M2 34V20C2 9 7 3 16 1l1 4c-5 2-7 5-7 9h8v20z" fill="#f1a14a"/><path d="M26 34V20c0-11 5-17 14-19l1 4c-5 2-7 5-7 9h8v20z" fill="#f7c898"/></svg>
    <p>Lorem ipsum dolor sit amet, consetetur sadipscing elitr, sed diam nonumy eirmod tempor invidunt ut labore et dolore magna aliquyam erat, sed diam voluptua. At vero eos et accusam et justo duo dolores et ea</p>
  </article>
  <article class="abs client-card" style="left:450px">
    <div class="client-head"><div class="avatar"><svg width="22" height="22" viewBox="0 0 22 22" fill="#5e6a7a"><circle cx="11" cy="7" r="5"/><path d="M1 22c0-6 4-9 10-9s10 3 10 9z"/></svg></div>
      <div><div class="client-name">Max Muster</div><div class="client-role">Sample Manager</div></div></div>
    <svg class="quote" width="48" height="36" viewBox="0 0 48 36"><path d="M2 34V20C2 9 7 3 16 1l1 4c-5 2-7 5-7 9h8v20z" fill="#f1a14a"/><path d="M26 34V20c0-11 5-17 14-19l1 4c-5 2-7 5-7 9h8v20z" fill="#f7c898"/></svg>
    <p>Lorem ipsum dolor sit amet, consetetur sadipscing elitr, sed diam nonumy eirmod tempor invidunt ut labore et dolore magna aliquyam erat, sed diam voluptua. At vero eos et accusam et justo duo dolores et ea</p>
  </article>
  <article class="abs client-card" style="left:776px">
    <div class="client-head"><div class="avatar"><svg width="22" height="22" viewBox="0 0 22 22" fill="#5e6a7a"><circle cx="11" cy="7" r="5"/><path d="M1 22c0-6 4-9 10-9s10 3 10 9z"/></svg></div>
      <div><div class="client-name">Max Muster</div><div class="client-role">Sample Manager</div></div></div>
    <svg class="quote" width="48" height="36" viewBox="0 0 48 36"><path d="M2 34V20C2 9 7 3 16 1l1 4c-5 2-7 5-7 9h8v20z" fill="#f1a14a"/><path d="M26 34V20c0-11 5-17 14-19l1 4c-5 2-7 5-7 9h8v20z" fill="#f7c898"/></svg>
    <p>Lorem ipsum dolor sit amet, consetetur sadipscing elitr, sed diam nonumy eirmod tempor invidunt ut labore et dolore magna aliquyam erat, sed diam voluptua. At vero eos et accusam et justo duo dolores et ea</p>
  </article>
</section>

<footer>
  <div class="abs footer-band"></div>
  <div class="abs brand footer-brand">
    <div class="brand-mark"></div>
    <div class="brand-name">KLARWEG COACHING</div>
  </div>
  <nav class="abs footer-nav"><a href="#">Home</a><a href="#">Leistungen</a><a href="#">Über mich</a><a href="#">Blog</a></nav>
  <div class="abs footer-social"><span></span><span></span></div>
  <div class="abs footer-rule"></div>
  <p class="abs copyright">© 2024 lindenhof-media.de</p>
  <nav class="abs legal"><a href="#">Impressum</a><a href="#">Datenschutz</a></nav>
</footer>

</body>
</html>
```